New Label Design Project for Tinkers hollow wines

I would like to purchase a customized version of a design you have previously submitted - https://www.artpitchhub.com.au/design/57302946

We need a label that that we can use for our new vintage shiraz, Merlot and Pinot Noir products. This Label will be just 1 label that will be front and back label.
Please see attached

Target Market(s)

young and old wine drinkers

Industry/Entity Type

Wine

Colors

Designer to choose colors to be used in the design.

Requirements
Must have
• logo but also is a bit funky
Nice to have
• mixture of Funky and Modern

```html
<!DOCTYPE html>
<html lang="en">
<head>
<meta charset="utf-8">
<title>Tinkers Hollow Wines – Shiraz Label</title>
<link rel="stylesheet" href="https://fonts.googleapis.com/css2?family=Pinyon+Script&family=Josefin+Sans:wght@300;400&display=swap">
<style>
  :root {
    --backdrop: #3a3a3a;
    --label-black: #121212;
    --pattern-tone: #1d1d1d;
    --gold: #c9a552;
    --gold-light: #e8cf8a;
    --gold-dark: #8a6a2a;
    --script-white: #f2f2f2;
    --band-dark: #141a20;
    --band-light: #26313b;
    --band-text: #e6e6e6;
  }
  * { margin: 0; padding: 0; box-sizing: border-box; }
  html, body {
    width: 1200px;
    height: 1006px;
    overflow: hidden;
    background: var(--backdrop);
  }
  .canvas {
    position: relative;
    width: 1200px;
    height: 1006px;
    background: radial-gradient(ellipse at center, #474747 0%, var(--backdrop) 70%);
  }
  .wine-label {
    position: absolute;
    left: 310px;
    top: 93px;
    width: 580px;
    height: 820px;
  }
  .label-shape {
    position: absolute;
    inset: 0;
    width: 100%;
    height: 100%;
  }
  .brand-mark {
    position: absolute;
    top: 118px;
    left: 0;
    width: 100%;
    text-align: center;
    font-family: "Josefin Sans", sans-serif;
    font-weight: 400;
    font-size: 22px;
    letter-spacing: 6px;
    color: var(--gold);
  }
  .wine-name {
    position: absolute;
    top: 210px;
    left: 0;
    width: 100%;
    text-align: center;
    font-family: "Pinyon Script", cursive;
    font-size: 82px;
    line-height: 84px;
    color: var(--script-white);
  }
  .vintage,
  .region {
    position: absolute;
    left: 0;
    width: 100%;
    text-align: center;
    font-family: "Josefin Sans", sans-serif;
    font-weight: 300;
    color: var(--gold);
  }
  .vintage { top: 478px; font-size: 44px; letter-spacing: 2px; }
  .region { top: 556px; font-size: 36px; letter-spacing: 2px; }
  .volume {
    position: absolute;
    top: 648px;
    left: 0;
    width: 100%;
    text-align: center;
    font-family: "Josefin Sans", sans-serif;
    font-weight: 300;
    font-size: 30px;
    color: var(--script-white);
  }
  .origin {
    position: absolute;
    top: 732px;
    left: 0;
    width: 100%;
    text-align: center;
    font-family: "Josefin Sans", sans-serif;
    font-weight: 300;
    font-size: 32px;
    letter-spacing: 1px;
    color: var(--band-text);
  }
</style>
</head>
<body>
<main class="canvas">
  <section class="wine-label">
    <svg class="label-shape" viewBox="0 0 580 820" xmlns="http://www.w3.org/2000/svg">
      <defs>
        <linearGradient id="goldEdge" x1="0" y1="0" x2="1" y2="1">
          <stop offset="0" stop-color="var(--gold-dark)"/>
          <stop offset="0.35" stop-color="var(--gold-light)"/>
          <stop offset="0.65" stop-color="var(--gold)"/>
          <stop offset="1" stop-color="var(--gold-dark)"/>
        </linearGradient>
        <linearGradient id="bandFill" x1="0" y1="0" x2="1" y2="0">
          <stop offset="0" stop-color="var(--band-dark)"/>
          <stop offset="0.6" stop-color="var(--band-light)"/>
          <stop offset="1" stop-color="var(--band-dark)"/>
        </linearGradient>
      </defs>
      <path class="label-border" d="M0,110 Q30,110 38,78 L130,78 Q200,4 290,4 Q380,4 450,78 L542,78 Q550,110 580,110 V820 H0 Z"
            fill="url(#goldEdge)"/>
      <path class="label-body" role="img" aria-label="Dark grapevine and scroll pattern across the label"
            d="M10,118 Q36,116 46,88 L134,88 Q204,16 290,16 Q376,16 446,88 L534,88 Q544,116 570,118 V810 H10 Z"
            fill="var(--label-black)"/>
      <rect class="pattern-tone" x="10" y="150" width="560" height="520" fill="var(--pattern-tone)" opacity="0.5"/>
      <line x1="10" y1="700" x2="570" y2="700" stroke="url(#goldEdge)" stroke-width="4"/>
      <rect class="origin-band" x="10" y="704" width="560" height="96" fill="url(#bandFill)"/>
      <rect x="0" y="800" width="580" height="20" fill="url(#goldEdge)"/>
    </svg>
    <div class="brand-mark">TINKERS HOLLOW</div>
    <h1 class="wine-name">Tinkers<br>Hollow</h1>
    <p class="vintage">2007 SHIRAZ</p>
    <p class="region">MT. BENSON</p>
    <p class="volume">750 ML</p>
    <p class="origin">WINE OF AUSTRALIA</p>
  </section>
</main>
</body>
</html>
```